We need a book cover design for a fitness professional's guidebook to be a successful trainer. LA celebrity trainer offers 7 ideas that are designed to transform any fitness professional's career and life. The cover design we are into is attached an includes the image of a man who is half dressed in a business suit and half dressed in fitness gear. The back photo should demonstrate the four sphere's the book is designed around (also attached) and will be included on the back with a brief description of the material (included below) and a short bio and photo of the writer (attached) at the very bottom. We'd like the book to have a work book feel, or text book geometry to it. The brand colors are Black and Red. The final design should invoke the feeling of success, health and happiness.

Dimensions: 8 5/8 x 5 3/4

USE WEBSITE AS REFERENCE FOR BRAND COLORS AND DESIGNS:
BravoMotion.net

BOOK TITLE:
RISING STRIDE
"A fitness professional's guidebook to be a successful trainer."

BACK COVER COPY:
Celebrity conditioning specialist and trainer consultant, Tavo Quintero, offers powerful ideas that are designed to transform every fitness professional's career and life. Reveal essential tools that every trainer and entrepreneur should know. Discover the deeper meaning of yourself and your career by working smarter rather than harder.

Find out how to create a brand, advertise it, and hone in on your market. Create buzz by landing magazine press. How to build celebrity clientele. Explore the world of multi-media projects. And finally, what to do when you reach your goals. This is an opportunity for trainer's to capture a share of the fitness industry’s vast $27B market. Fulfill your fullest earning potential while also understanding what the true meaning of success is, and how to achieve it. Learn what you love to do, what you do well, what the fitness industry needs and what it will pay for.

Aimed at the trainers who want to know the mistakes to avoid, and the habits to establish that will set them apart from the rest, Rising Stride is THE guidebook that has the power to take your career and life in the direction that will prepare you for continued success. Use these business ideas to promote your passive income, generate multiple streams of revenue and increase your investments, resulting in more freedom and access in the fitness industry and beyond. Let Rising Stride unleash your potential to be a successful trainer.

BACK AUTHOR BIO:
Los Angeles based celebrity trainer and trainer consultant, Tavo Quintero, CSCS, developed his very own “Anchor” technique and fitness brand. Quintero’s clients include a mix of celebrities, professional athletes, musicians, fashion models, students, political figures and corporate professionals. Vigor magazine described Quintero’s fitness DVD, TAVOMOVE, as “a workout you’ll look forward to”. Tavo was also the co-developer of a natural energy drink that increases energy and metabolism with an ancient Peruvian super food. Additionally backed by his finance and advertising education, Tavo has consulted several trainers and fitness brands to guide them to their maximum earning potential.

Target Market(s)

Fitness Industry/Trainers

Industry/Entity Type

Advertising

Requirements
Must have
• Consistent with website logo colors, shapes and fonts.

```html
<!DOCTYPE html>
<html lang="en">
<head>
<meta charset="utf-8">
<title>Rising Stride — Book Cover</title>
<link rel="stylesheet" href="https://fonts.googleapis.com/css2?family=Josefin+Sans:wght@400;600;700&family=Didact+Gothic&display=swap">
<style>
  :root {
    --red: #ee4540;
    --black: #0d0d0d;
    --white: #ffffff;
    --paper-light: #f4f4f5;
    --paper-mid: #d9d9dc;
    --ink: #111111;
    --display: "Josefin Sans", sans-serif;
    --body: "Didact Gothic", sans-serif;
  }
  * { box-sizing: border-box; margin: 0; padding: 0; }
  html, body { width: 1200px; height: 867px; overflow: hidden; background: #ffffff; }
  .cover { position: relative; width: 1200px; height: 867px; display: flex; }

  /* Back cover */
  .back { position: relative; width: 570px; height: 867px; background: var(--red); color: var(--white); }
  .back-title { position: absolute; left: 100px; top: 58px; font-family: var(--display); font-weight: 400; font-size: 48px; letter-spacing: 0; line-height: 1; }
  .back-title .accent { color: var(--black); }
  .back-copy { position: absolute; left: 56px; top: 138px; width: 500px; font-family: var(--body); font-size: 12.6px; line-height: 17.4px; text-align: justify; }
  .back-copy p + p { margin-top: 17px; }
  .author-box { position: absolute; left: 56px; top: 590px; width: 514px; height: 202px; background: var(--black); }
  .author-photo { position: absolute; left: 13px; top: 10px; width: 150px; height: 150px; background: linear-gradient(160deg, #8e8f92 0%, #5a4e46 55%, #2a2a2c 100%); }
  .author-bio { position: absolute; left: 173px; top: 10px; width: 326px; font-family: var(--body); font-size: 10.2px; line-height: 13.3px; text-align: justify; color: var(--white); }
  .website { position: absolute; left: 0; width: 570px; top: 810px; text-align: center; font-family: var(--body); font-size: 15px; letter-spacing: 2.5px; }

  /* Spine */
  .spine { position: relative; width: 55px; height: 867px; background: var(--black); }
  .spine-title, .spine-author { position: absolute; left: 50%; white-space: nowrap; transform-origin: center; font-family: var(--display); }
  .spine-title { top: 260px; transform: translate(-50%, -50%) rotate(90deg); font-size: 38px; color: var(--white); }
  .spine-title .accent { color: var(--red); }
  .spine-author { top: 720px; transform: translate(-50%, -50%) rotate(90deg); font-size: 22px; font-variant: small-caps; letter-spacing: 2px; color: var(--white); }

  /* Front cover */
  .front { position: relative; width: 575px; height: 867px; background: radial-gradient(ellipse at 55% 45%, var(--paper-light) 0%, var(--paper-mid) 100%); }
  .front-title { position: absolute; left: 0; width: 575px; top: 52px; text-align: center; font-family: var(--display); font-weight: 400; font-size: 112px; line-height: 94px; }
  .front-title .line-one { display: block; color: var(--ink); }
  .front-title .line-two { display: block; color: var(--red); }
  .hero-photo { position: absolute; left: 28px; top: 270px; width: 545px; height: 345px; background: radial-gradient(ellipse at 60% 55%, #c7c7ca 0%, #e2e2e4 60%, rgba(226,226,228,0) 100%); }
  .subtitle { position: absolute; left: 0; width: 575px; top: 628px; text-align: center; font-family: var(--display); color: var(--ink); }
  .subtitle-lead { display: block; font-size: 19px; font-weight: 400; letter-spacing: 0.5px; }
  .subtitle-main { display: block; margin-top: 4px; font-size: 27px; font-weight: 700; letter-spacing: 0.5px; }
  .rule { position: absolute; left: 42px; top: 700px; }
  .front-author { position: absolute; left: 0; width: 575px; top: 762px; text-align: center; font-family: var(--display); font-size: 52px; font-variant: small-caps; letter-spacing: 4px; color: var(--ink); }
</style>
</head>
<body>
<div class="cover">
  <section class="back">
    <h2 class="back-title">RISING<span class="accent">STRIDE</span></h2>
    <div class="back-copy">
      <p>Celebrity conditioning specialist and trainer consultant, Tavo Quintero, offers powerful ideas that are designed to transform every fitness professional's career and life. Reveal essential tools that every trainer and entrepreneur should know. Discover the deeper meaning of yourself and your career by working smarter rather than harder.</p>
      <p>Find out how to create a brand, advertise it, and hone in on your market. Create buzz by landing magazine press. How to build celebrity clientele. Explore the world of multi-media projects. And finally, what to do when you reach your goals. This is an opportunity for trainer's to capture a share of the fitness industry’s vast $27B market. Fulfill your fullest earning potential while also understanding what the true meaning of success is, and how to achieve it. Learn what you love to do, what you do well, what the fitness industry needs and what it will pay for.</p>
      <p>Aimed at the trainers who want to know the mistakes to avoid, and the habits to establish that will set them apart from the rest, Rising Stride is THE guidebook that has the power to take your career and life in the direction that will prepare you for continued success. Use these business ideas to promote your passive income, generate multiple streams of revenue and increase your investments, resulting in more freedom and access in the fitness industry and beyond. Let Rising Stride unleash your potential to be a successful trainer.</p>
    </div>
    <div class="author-box">
      <div class="author-photo" role="img" aria-label="Portrait of the author seated outdoors with a city skyline behind"></div>
      <p class="author-bio">Los Angeles based celebrity trainer and trainer consultant, Tavo Quintero, CSCS, developed his very own “Anchor” technique and fitness brand. Quintero’s clients include a mix of celebrities, professional athletes, musicians, fashion models, students, political figures and corporate professionals. Vigor magazine described Quintero’s fitness DVD, TAVOMOVE, as “a workout you’ll look forward to”. Tavo was also the co-developer of a natural energy drink that increases energy and metabolism with an ancient Peruvian super food. Additionally backed by his finance and advertising education, Tavo has consulted several trainers and fitness brands to guide them to their maximum earning potential.</p>
    </div>
    <p class="website">www.bravomotion.net</p>
  </section>

  <section class="spine">
    <span class="spine-title">RISING<span class="accent">STRIDE</span></span>
    <span class="spine-author">Tavo Quintero</span>
  </section>

  <section class="front">
    <h1 class="front-title"><span class="line-one">RISING</span><span class="line-two">STRIDE</span></h1>
    <div class="hero-photo" role="img" aria-label="Athletic woman in workout gear stretching on the floor, reaching toward her red running shoes, with small dumbbells beside her"></div>
    <p class="subtitle">
      <span class="subtitle-lead">A FITNESS PROFESSIONAL’S GUIDEBOOK</span>
      <span class="subtitle-main">TO BE A SUCCESSFUL TRAINER</span>
    </p>
    <svg class="rule" width="500" height="4" viewBox="0 0 500 4" aria-hidden="true">
      <rect x="0" y="0" width="500" height="3" fill="var(--red)"/>
    </svg>
    <p class="front-author">Tavo Quintero</p>
  </section>
</div>
</body>
</html>
```